New Stationery and envelope Design Project

I need business envelopes and stationary. I would like to have office locations on both (only Chicago address) which are Chicago (Oak Brook), Washington, Mexico City, Bogota. Of course in formats I can upload and have printed. Simple and very professional I am looking for. The return address/stationary address should be:

2867 North Pellam Avenue
Annex Level
Rivermont, Illinois 60871

Target Market(s)

I am a consultant for larger corporations

Industry/Entity Type

Consulting

Colors

Designer to choose colors to be used in the design.

Requirements
Must have
• our address, logo, very professional and clean.
Nice to have
• the names of the cities we have offices.

```html
<!DOCTYPE html>
<html lang="en">
<head>
<meta charset="utf-8">
<title>Lakeshore Meridian – Letterhead and Envelope</title>
<link href="https://fonts.googleapis.com/css2?family=Fira+Sans:wght@500&family=Roboto:wght@400&family=Raleway:wght@400&display=swap" rel="stylesheet">
<style>
  :root {
    --backdrop: #737373;
    --paper: #efefef;
    --brand-blue: #1652b8;
    --flap-blue: #0b52b8;
    --mark-blue: #2a9be6;
    --ink: #444444;
    --ink-soft: #555555;
    --rule: #9a9a9a;
    --signature: #dbe6f5;
    --shadow: rgba(0, 0, 0, 0.28);
  }
  * { margin: 0; padding: 0; box-sizing: border-box; }
  html, body { width: 1200px; height: 947px; overflow: hidden; background: var(--backdrop); }
  .canvas { position: relative; width: 1200px; height: 947px; }

  .letterhead {
    position: absolute; left: 72px; top: 82px; width: 553px; height: 780px;
    background: var(--paper);
  }
  .brand { position: absolute; display: flex; align-items: center; gap: 6px; }
  .brand-dot { width: 9px; height: 9px; border-radius: 50%; background: var(--mark-blue); flex: none; }
  .brand-name {
    font-family: "Fira Sans", sans-serif; font-weight: 500; color: var(--brand-blue);
    font-size: 12.5px; line-height: 14px; white-space: nowrap;
  }
  .letterhead .brand { left: 40px; top: 98px; }

  .address {
    font-family: "Roboto", sans-serif; font-weight: 400; font-style: normal;
    font-size: 8.6px; line-height: 10.4px; color: var(--ink); white-space: nowrap;
  }
  .letterhead .address {
    position: absolute; left: 402px; top: 78px; padding: 2px 0 2px 7px;
    border-left: 1px solid var(--rule);
  }

  .salutation {
    position: absolute; left: 59px; top: 212px;
    font-family: "Raleway", sans-serif; font-weight: 400; font-size: 13.5px; line-height: 16px; color: var(--ink);
  }
  .letter-body {
    position: absolute; left: 59px; top: 254px; width: 439px;
    font-family: "Raleway", sans-serif; font-weight: 400; font-size: 7.6px; line-height: 11.4px;
    color: var(--ink-soft); text-align: left;
  }
  .letter-body p + p { margin-top: 11.4px; }
  .closing {
    position: absolute; left: 59px; top: 492px;
    font-family: "Raleway", sans-serif; font-size: 7.6px; line-height: 10px; color: var(--ink-soft);
  }
  .signature {
    position: absolute; left: 56px; top: 526px; width: 92px; height: 36px;
    background: var(--signature); border-radius: 4px;
  }

  .offices {
    position: absolute; font-family: "Roboto", sans-serif; font-weight: 400; font-size: 8px; line-height: 10px;
    color: var(--brand-blue); white-space: nowrap; transform: translateX(-50%);
  }
  .letterhead .offices { left: 284px; top: 751px; }

  .envelope-back {
    position: absolute; left: 570px; top: 381px; width: 579px; height: 289px;
    background: var(--paper); box-shadow: -2px 2px 10px var(--shadow);
  }
  .envelope-back svg { position: absolute; left: 0; top: 0; }

  .envelope-front {
    position: absolute; left: 475px; top: 531px; width: 634px; height: 290px;
    background: var(--paper); box-shadow: -2px 2px 10px var(--shadow);
  }
  .envelope-front .brand { left: 22px; top: 88px; }
  .envelope-front .address { position: absolute; left: 22px; top: 107px; }
  .envelope-front .offices { left: 305px; top: 258px; }
</style>
</head>
<body>
<main class="canvas">

  <section class="letterhead">
    <div class="brand">
      <span class="brand-dot"></span>
      <span class="brand-name">LAKESHORE MERIDIAN</span>
    </div>
    <address class="address">
      2867 North Pellam Avenue<br>
      Annex Level<br>
      Rivermont, Illinois 60871
    </address>

    <p class="salutation">Dear Mr. Harlow,</p>
    <div class="letter-body">
      <p>Lorem ipsum dolor sit amet, consectetur adipiscing elit. Donec orci purus, luctus vitae dignissim eu, iaculis sed purus. Vivamus faucibus, ipsum nec aliquet viverra, leo mauris condimentum ligula, sit amet sagittis enim ligula quis arcu. Nam egestas tortor id nisi porttitor mattis. In tortor ante, ultricies in suscipit a, tempus non massa. Vivamus et auctor mi. Fusce vel massa nulla. Phasellus nec eros mauris, et scelerisque orci.</p>
      <p>Donec malesuada orci vitae nulla accumsan porta a id massa. Quisque accumsan iaculis magna sit amet fringilla. Maecenas consequat, magna eget tincidunt semper, odio nibh rutrum mi, id feugiat ante nisi eu risus. Vestibulum nunc orci, rhoncus a placerat in, ultricies in mi. Cras mattis varius eros, vel fringilla nisi suscipit eget. Quisque scelerisque sagittis nulla at porttitor.</p>
      <p>Sed id augue vitae urna euismod commodo aliquet a quam. Pellentesque arcu velit, cursus et malesuada ut, consequat et diam. Nullam erat sem, rhoncus id ullamcorper vitae, rhoncus et arcu. In ultricies ultricies nulla, ut rutrum nisi iaculis at. Donec eu magna a metus ornare faucibus. Fusce aliquet faucibus ultricies. Morbi semper, est id tincidunt gravida, sem arcu adipiscing lacus, ac bibendum nulla leo eu purus. Quisque nec diam sed risus consectetur accumsan quis quis nibh. Vestibulum id purus lorem.</p>
      <p>It is a long established fact that a reader will be distracted by the readable content of a page when looking at its layout. The point of using Lorem Ipsum is that it has a more-or-less normal distribution of letters, as opposed to using 'Content here, content here', making it look like readable English. Many desktop publishing packages use it.</p>
    </div>
    <p class="closing">Sincerely,</p>
    <div class="signature" role="img" aria-label="Handwritten signature of James Harlow"></div>

    <p class="offices">Lakeport (Rivermont) | Easton | Valle Alto | Serrana</p>
  </section>

  <section class="envelope-back">
    <svg width="579" height="289" viewBox="0 0 579 289" aria-hidden="true">
      <path d="M0 0 H579 L568 70 Q565 85 548 85 H36 Q22 85 18 70 Z" fill="var(--flap-blue)"/>
    </svg>
  </section>

  <section class="envelope-front">
    <div class="brand">
      <span class="brand-dot"></span>
      <span class="brand-name">LAKESHORE MERIDIAN</span>
    </div>
    <address class="address">
      2867 North Pellam Avenue<br>
      Annex Level<br>
      Rivermont, Illinois 60871
    </address>
    <p class="offices">Lakeport (Rivermont) | Easton | Valle Alto | Serrana</p>
  </section>

</main>
</body>
</html>
```